Attractive Flyer for Moving Company

Our Company is called "Harborline Haulers".
We provide moving service for home and businesses
We need a flyer for a moving company, located in South Florida USA
Flyer size will be 7 x 5 inches, double sided.

Flyer needs to be very attractive and catchy for eye. I want people to keep it even if they don't need our service. I attached a lot of text in separate word file.
Logo, brief and additional pictures are attached.

```html
<!DOCTYPE html>
<html lang="en">
<head>
<meta charset="utf-8">
<title>Harborline Haulers Flyer</title>
<link rel="stylesheet" href="https://fonts.googleapis.com/css2?family=Exo+2:ital,wght@1,800&family=Nunito+Sans:ital,wght@0,400;0,600;0,700;0,800;1,400&display=swap">
<style>
:root{
  --red:#c41e2e;
  --ink:#1d1d1f;
  --muted:#6a6a6a;
  --paper:#ffffff;
  --board:#ffffff;
  --wall:#f4f0eb;
  --denim:#9fb0c2;
  --cardboard:#caa67b;
  --floor:#d9c7b2;
  --box-light:#e3cba6;
  --box-dark:#c4a276;
}
*{box-sizing:border-box;margin:0;padding:0}
html,body{width:1200px;height:675px;overflow:hidden;background:var(--board)}
body{font-family:"Nunito Sans",Arial,sans-serif;color:var(--ink);position:relative}
.page{position:absolute;top:127px;width:300px;height:420px;background:var(--paper);overflow:hidden;box-shadow:0 0 0 1px #e2e2e2}
.front{left:270px}
.back{left:630px}

/* front */
.front-photo{position:absolute;inset:0;background:linear-gradient(200deg,var(--wall) 0%,var(--wall) 28%,#e6dfd7 40%,var(--denim) 62%,var(--cardboard) 80%,var(--floor) 100%)}
.headline{position:absolute;top:16px;right:14px;width:210px;text-align:center;font-family:"Exo 2",Arial,sans-serif;font-style:italic;font-weight:800;font-size:27px;line-height:1.12;color:var(--red)}
.promo{position:absolute;top:82px;right:22px;width:172px;text-align:center;font-size:8px;line-height:1.35}
.promo .ask{font-weight:700;display:block}
.promo .date{color:var(--red);font-weight:700}
.front-brand{position:absolute;right:14px;bottom:36px;display:flex;align-items:center;gap:5px;font-weight:800;font-size:13px;color:var(--red)}
.front-brand .dot{width:10px;height:10px;border-radius:50%;background:var(--red)}
.license{position:absolute;right:12px;bottom:8px;text-align:right;font-size:6px;line-height:1.4;color:#4a4a4a}

/* back */
.services{position:absolute;top:52px;left:0;right:0;text-align:center;font-style:italic;font-size:8px;line-height:1.5;color:var(--ink)}
.services .label,.services .sep{color:var(--red)}
.why{position:absolute;top:104px;left:18px;font-size:8.8px;line-height:1.42}
.why h2{font-size:9.5px;font-weight:800;color:var(--red)}
.why ul{list-style:none}
.why li::before{content:"•";color:var(--red);margin-right:4px}
.badge{position:absolute;top:258px;left:16px;width:52px;height:52px;border-radius:50%;background:var(--red)}
.trust{position:absolute;top:318px;left:18px;font-style:italic;font-size:7.5px;line-height:1.35;color:var(--muted)}
.contact{position:absolute;top:348px;left:18px;font-size:7.5px;line-height:1.4}
.boxes{position:absolute;right:14px;top:203px;width:124px;height:186px;background:linear-gradient(180deg,var(--box-light),var(--box-dark));clip-path:polygon(48% 0,100% 0,100% 33%,100% 100%,0 100%,0 62%,13% 62%,13% 38%,22% 38%,22% 28%,48% 28%)}
.back-brand{position:absolute;right:22px;top:370px;font-weight:800;font-size:7px;color:var(--ink)}
.band{position:absolute;left:0;right:0;bottom:0;height:21px;background:var(--red)}
</style>
</head>
<body>
<section class="page front">
  <div class="front-photo" role="img" aria-label="Photo of a happy family lifting their baby among moving boxes in a bright room"></div>
  <h1 class="headline">“Where Speed Meets Quality”</h1>
  <p class="promo"><span class="ask">“MOVING SOON?”</span>Not moving soon? Keep this flyer for later and/or share it with friends. Promotion is valid until <span class="date">January 1st, 2020</span></p>
  <div class="front-brand"><span class="dot"></span>Harborline Haulers</div>
  <p class="license">Licensed &amp; Fully Insured,<br>FL MOVERS LICENSE#: IM5172 US DOT: #4418206</p>
</section>

<section class="page back">
  <p class="services"><span class="label">Moving Services:</span> Residential <span class="sep">•</span> Long Distance <span class="sep">•</span> Commercial Loading<br><span class="sep">•</span> Unloading rental truck <span class="sep">•</span> Portable storage <span class="sep">•</span> Packing Service</p>
  <div class="why">
    <h2>Why Call Us?</h2>
    <ul>
      <li>Customer Service Oriented</li>
      <li>Years of Great reputation (Lots of 5 Star Reviews)</li>
      <li>Affordable pricing</li>
      <li>Professional, efficient, strong movers</li>
      <li>We always handle your belongings with care</li>
      <li>Clean and equipped trucks</li>
      <li>Absolutely NO hidden fees</li>
    </ul>
  </div>
  <div class="badge" role="img" aria-label="Review site badge"></div>
  <p class="trust">Chamber Accredited Business,<br>People Love us on ReviewHub</p>
  <p class="contact">CALL FOR A QUICK ESTIMATE<br>Toll Free: (800) 555-0148<br>Or Request Your Estimate online<br>www.harborlinehaulers.com</p>
  <div class="boxes" role="img" aria-label="Illustration of a stack of cardboard moving boxes with a cap on top"></div>
  <div class="back-brand">Harborline Haulers</div>
  <div class="band"></div>
</section>
</body>
</html>
```